Canned mixed vegetables and sweet corn for MOLAN

We need packaging design for two products under the MOLAN brand: canned mixed vegetables and sweet corn.

Mixed Vegetables Label:
Product: Canned Mixed Vegetables
Brand: MOLA
Sweet Corn Label:
Product: Canned Sweet Corn
Brand: MOLA
Please ensure the following elements are incorporated into the label designs:

1-Branding:
Prominently feature the brand name "Molan" on both labels to establish brand identity we'll include the logo at the end of this text.
Product Name:
Clearly display the product names, "Mixed Vegetables" and "Sweet Corn," on their respective labels and in French "Macedoine of vegetables" and "Mais in grain"
Visuals:
Include appealing and high-quality images of the mixed vegetables and sweet corn on their respective labels. These images should accurately represent the product.
Mockup size: 325mmx104mm
Ingredients:
List the ingredients used in the canned mixed vegetables and sweet corn on their respective labels. Ensure the ingredient list is legible and easy to read and it has to be in french and english.
Ingredients (sweet corn):-EN: Whole kernel corn, water, salt.
-EN: Whole grain corn, water, salt.
Ingredients (mixed vegetables): -EN: carrots, garden peas, sweet corn, green beans.
-EN: mixed vegetables, carrots, peas, corn, green beans
BARCODE:
Please leave space for the barcode.

Nutrition Facts:
Provide the nutritional information for both products on their respective labels. Include details such as serving size, calories, fat content, carbohydrate content, protein content, and any other relevant nutritional information the examples are below this text
Additional Details:
Include any relevant information about the products, such as natural and fresh
Compliance:
Ensure that the labels comply with all relevant labeling regulations and requirements.
Please collaborate with a graphic designer to create visually appealing label designs that align with the Molan brand and effectively communicate the necessary product information.

Industry/Entity Type

agri-food

Font styles to use
Decorative
Script

Colors
59FF00
82FF00
B8FF75
E3FFCB
F4FFEA
FFF300
FFF600
FEFA6F
FFFEC7
FFFEE8
FFC000
F8CF3A
FAE287
FDF2CF
FEFAEE
F0912C
F2A743
F7CA91
FBE8D2
FDF5EE
EE7325
F08F49
F5BC92
FAE3D3
FDF4ED
EB3D1F
EC4F4E
F09395
F8D3D4
FCEDEE
E54698
E96AAD
F1A4CE
F9D9EA
FCEFF6
A7469A
B969AE
D3A5CF
EDDBEB
F8F0F9

Requirements
Must have
• 1-LOGO 2- Product Name in EN and FR. 3- Ingredients 4- Barcode. 5-Nutrition facts. 6- Fresh vegetables image
Nice to have
• Ensure that the labels comply with all relevant labeling regulations and requirements.

```html
<!DOCTYPE html>
<html lang="en">
<head>
<meta charset="utf-8">
<title>MOLAN canned vegetables labels</title>
<link rel="stylesheet" href="https://fonts.googleapis.com/css2?family=Arimo:wght@700&family=Special+Elite&display=swap">
<style>
  :root {
    --backdrop: #e4e4e4;
    --gold: #ddd596;
    --gold-dark: #c9bf6e;
    --green: #1fa35f;
    --green-line: #2fb071;
    --navy: #3e3f78;
    --white: #ffffff;
    --corn-1: #ffe14a;
    --corn-2: #f5b81e;
    --veg-green: #4f8f3a;
    --veg-orange: #f08f49;
  }
  * { box-sizing: border-box; margin: 0; padding: 0; }
  html, body { width: 1200px; height: 1200px; overflow: hidden; }
  body {
    background: var(--backdrop);
    position: relative;
    font-family: "Arimo", Arial, sans-serif;
  }
  .label {
    position: absolute;
    top: 320px;
    width: 410px;
    height: 580px;
    background: var(--white);
    overflow: hidden;
    box-shadow: 0 6px 20px rgba(0,0,0,0.12);
  }
  .label--corn { left: 160px; }
  .label--veg { left: 630px; }
  .band { position: absolute; left: 0; right: 0; background: var(--gold); }
  .band--top { top: 0; height: 36px; border-bottom: 6px solid var(--green-line); }
  .band--bottom { bottom: 0; height: 30px; border-top: 6px solid var(--green-line); }
  .product-photo {
    position: absolute;
    left: 0; right: 0;
    top: 150px;
    height: 370px;
  }
  .label--corn .product-photo {
    background: radial-gradient(ellipse at 65% 40%, var(--corn-1) 0%, #fbd13a 35%, rgba(245,184,30,0.5) 60%, rgba(255,255,255,0) 80%),
                linear-gradient(90deg, rgba(245,184,30,0.7) 0%, rgba(255,255,255,0) 35%);
  }
  .label--veg .product-photo {
    background: radial-gradient(ellipse at 68% 35%, var(--veg-green) 0%, #6aa544 30%, rgba(240,143,73,0.55) 55%, rgba(255,255,255,0) 80%),
                linear-gradient(200deg, rgba(255,255,255,0) 60%, rgba(240,143,73,0.7) 100%);
  }
  .brand {
    position: absolute;
    top: 72px; left: 0; right: 0;
    text-align: center;
    display: flex; justify-content: center; align-items: center; gap: 14px;
  }
  .brand__dot { width: 22px; height: 22px; border-radius: 50%; background: var(--green); }
  .brand__name {
    font-family: "Arimo", Arial, sans-serif;
    font-weight: 700;
    font-size: 72px;
    color: var(--navy);
    letter-spacing: 1px;
  }
  .fresh-badge {
    position: absolute;
    top: 300px; left: 26px;
    width: 82px; height: 82px;
    border-radius: 50%;
    background: var(--green);
    color: var(--white);
    font-family: "Special Elite", "Courier New", monospace;
    font-size: 10px;
    line-height: 1.3;
    text-align: center;
    display: flex; align-items: center; justify-content: center;
  }
  .product-name {
    position: absolute;
    left: 36px; right: 36px;
    top: 410px;
    height: 104px;
    background: var(--green);
    border: 4px solid var(--gold);
    border-radius: 12px;
    color: var(--white);
    font-family: "Special Elite", "Courier New", monospace;
    text-align: center;
    display: flex; flex-direction: column; justify-content: center;
  }
  .product-name__en { font-size: 30px; line-height: 1.15; }
  .product-name__fr { font-size: 18px; line-height: 1.3; }
  .label--veg .product-name__en { font-size: 24px; }
  .label--veg .product-name__fr { font-size: 14px; }
  .net-weight {
    position: absolute;
    bottom: 44px; left: 0; right: 0;
    text-align: center;
    font-weight: 700;
    font-size: 16px;
    color: var(--navy);
  }
</style>
</head>
<body>
  <section class="label label--corn">
    <div class="band band--top"></div>
    <div class="product-photo" role="img" aria-label="Photo of sweet corn kernels in a white bowl beside a corn cob"></div>
    <div class="brand"><span class="brand__dot"></span><span class="brand__name">MOLAN</span></div>
    <div class="fresh-badge">LOCKED<br>IN<br>FRESHNESS</div>
    <div class="product-name">
      <span class="product-name__en">SWEET CORN</span>
      <span class="product-name__fr">MAIS IN GRAIN</span>
    </div>
    <div class="net-weight">250g NET.WT.</div>
    <div class="band band--bottom"></div>
  </section>

  <section class="label label--veg">
    <div class="band band--top"></div>
    <div class="product-photo" role="img" aria-label="Photo of mixed green beans, peas and diced carrots on a white plate with pea pods and carrot slices"></div>
    <div class="brand"><span class="brand__dot"></span><span class="brand__name">MOLAN</span></div>
    <div class="fresh-badge">LOCKED<br>IN<br>FRESHNESS</div>
    <div class="product-name">
      <span class="product-name__en">MIXED VEGETABLES</span>
      <span class="product-name__fr">MACEDOINE OF VEGETABLES</span>
    </div>
    <div class="net-weight">250g NET.WT.</div>
    <div class="band band--bottom"></div>
  </section>
</body>
</html>
```